Clinician Supply Circle

I am a financial planner whose client's are physicians and dentists. As physicians, there is very little time for them to do research on numerous aspects of their business and personal lives. I am looking to build a website that is a 1 stop shop for many of the services/resources they may need. It will be my job to screen the resources/advertisers and place competent people/business's that I know and have a track record on. there will ultimately be 10 or 12 ish areas that I would like to provide resources in:
disability insurance
life insurance
retirement planning
student loan advisors
employment contract and business formation attorneys
accountants
real estate agents
physician mortgages
personal loans
malpractice insurance
physician recruiters
maybe 2 other areas which I have yet to figure out.....
I would like each of these options to be able to be clicked on and a page will open up with the 1 or 2 or 3 or 4 people/business's that I have picked to represent these areas. I would like each specific person/business to have a click here to contact me link in which an email goes to the person and I am copied on the initial correspondence between the physician and the mortgage broker.... just so I can see some of the correspondence they will be receiving.
nowhere on the site do I want it to say my name. there will be certain disclosures that are needed and other wording but I think this is a good starting point.
here are links to two websites with the same general concept. please keep in mind that I want my website to be more on the simple side.
http://www.quillbarrowpartners.example/index.html
http://fernlakeledger.example/
Updates
Industry/Entity Type
Financial

```html
<!DOCTYPE html>
<html lang="en">
<head>
<meta charset="utf-8">
<title>Clinician Supply Circle</title>
<link href="https://fonts.googleapis.com/css2?family=Fauna+One&family=Gentium+Book+Plus:wght@400;700&family=Arimo&display=swap" rel="stylesheet">
<style>
:root{
  --green:#2fbf4f;
  --green-dark:#1e9a3a;
  --ink:#555;
  --ink-dark:#333;
  --bar:#222;
  --page:#f4f4f4;
  --white:#fff;
  --footer:#5c5c5c;
  --footer-line:#8a8a8a;
}
*{margin:0;padding:0;box-sizing:border-box}
html,body{width:1200px;height:900px;overflow:hidden}
body{position:relative;background:var(--page);font-family:"Gentium Book Plus",serif;color:var(--ink)}
.abs{position:absolute}
ul{list-style:none}

/* admin bar */
.admin-bar{left:0;top:0;width:1200px;height:14px;background:var(--bar);color:#ddd;font:7px "Arimo",sans-serif}
.admin-bar span{position:absolute;top:3px}
.admin-dot{width:10px;height:10px;border-radius:50%;background:#777;left:7px;top:2px!important}
.admin-help{left:1047px;top:0!important;height:14px;width:47px;background:#6a9a3a;color:#fff;text-align:center;line-height:14px}
.admin-avatar{left:1157px;top:3px!important;width:12px;height:8px;background:#ddd}

/* header */
.site-header{left:0;top:14px;width:1200px;height:58px;background:var(--white);box-shadow:0 2px 3px rgba(0,0,0,.12)}
.brand{left:62px;top:20px;display:flex;align-items:center;gap:7px;color:var(--ink-dark);font-family:"Gentium Book Plus",serif;font-size:16px;line-height:18px;white-space:nowrap}
.brand-dot{width:12px;height:12px;border-radius:50%;background:var(--green)}
.nav-panel{left:312px;top:8px;width:878px;height:38px;background:var(--white);box-shadow:0 1px 3px rgba(0,0,0,.25)}
.social{display:flex;gap:12px}
.social i{width:9px;height:9px;border-radius:50%;background:#8a8a8a;display:block}
.nav-panel .social{position:absolute;left:20px;top:6px}
.tagline{right:12px;top:3px;color:var(--green);font-style:italic;font-weight:700;font-size:11px}
.main-nav{left:22px;top:24px;display:flex;font-family:"Fauna One",serif;font-size:10px;color:#777}
.main-nav li{margin-right:30px}
.main-nav .current{color:var(--green)}

/* slider */
.hero{left:155px;top:77px;width:889px;height:230px;background:linear-gradient(110deg,#1e1f22 0%,#2e2f32 35%,#6a6a68 60%,#cfcfcb 80%,#e6e6e2 100%)}
.hero-caption{left:98px;top:78px;width:622px;height:100px;background:rgba(40,40,40,.45)}
.hero h1{left:144px;top:77px;color:var(--white);font-family:"Fauna One",serif;font-weight:400;font-size:22px;line-height:26px}
.hero p{left:144px;top:101px;width:515px;color:var(--white);font-size:13.5px;line-height:12px}
.btn{display:block;background:linear-gradient(var(--green),var(--green-dark));color:var(--white);font:9px "Arimo",sans-serif;text-align:center;border-radius:2px}
.hero .btn{left:143px;top:131px;width:112px;height:20px;line-height:20px}
.arrow{top:100px;width:16px;height:26px}
.edit-tag{background:#2d2d2d;color:#ddd;font:5px "Arimo",sans-serif;text-align:center;border-radius:2px}
.hero .edit-tag{left:816px;top:198px;width:34px;height:13px;line-height:13px;border:1px solid #666}

/* features */
.feature{top:343px;width:260px;text-align:center}
.feature .thumb{width:130px;height:80px;border-radius:50%;margin:0 auto}
.thumb-service{background:linear-gradient(180deg,#fdfdfd 0%,#f2f2f2 30%,#9a9a9a 48%,#6a6a6a 58%,#d8d8d8 72%,#fafafa 100%)}
.thumb-planning{background:linear-gradient(180deg,#e8f2fc 0%,#3a8ee8 22%,#1a62d0 55%,#6fb0f0 80%,#eaf3fc 100%)}
.thumb-blog{background:linear-gradient(180deg,#ffffff 0%,#ffffff 25%,#3a4aa8 40%,#1c2a8a 58%,#ffffff 70%,#6a74c0 85%,#ffffff 100%)}
.feature h2{margin-top:21px;font-family:"Fauna One",serif;font-weight:400;font-size:18px;line-height:20px;color:#444}
.feature h2 .edit-tag{display:inline-block;width:22px;height:9px;line-height:9px;vertical-align:middle;margin-left:4px}
.feature p{font-size:8.8px;line-height:9.5px;margin:2px auto 0;width:262px;color:#444}
.feature .btn{width:78px;height:15px;line-height:15px;margin:6px auto 0;font-size:8px}
.rule{left:155px;top:533px;width:889px;height:1px;background:#e2e2e2}

/* sidebar */
.sidebar{left:155px;top:550px;width:204px;border-right:1px solid #e2e2e2;height:168px}
.sidebar h3{font-family:"Fauna One",serif;font-weight:400;font-size:14px;color:#444;display:flex;align-items:center;gap:8px}
.sidebar li{font-size:8px;color:var(--green);padding:1px 0 1px 15px;border-bottom:1px solid #e6e6e6;height:12.4px;position:relative;margin-left:13px}
.sidebar li::before{content:"›";position:absolute;left:2px;top:-1px}
.intro{left:383px;top:548px;width:662px;font-size:9.3px;line-height:9.5px;color:#444}
.intro p{margin-bottom:3px}

/* footer */
.site-footer{left:0;top:733px;width:1200px;height:144px;background:var(--footer);border-top:3px solid #d8d8d8}
.site-footer h4{font-family:"Fauna One",serif;font-weight:400;font-size:13px;color:var(--white);text-align:center}
.recent{left:155px;top:14px;width:278px}
.recent li{font-size:7px;color:var(--white);padding:1px 0 1px 10px;border-bottom:1px solid var(--footer-line);position:relative}
.recent li::before,.footer-links li::before{content:"›";position:absolute;left:0;top:0;color:var(--green)}
.disclosure{left:459px;top:14px;width:280px}
.disclosure p{font:7.6px "Arimo",sans-serif;line-height:9.5px;color:var(--white);margin-top:4px}
.footer-links{left:762px;top:11px}
.footer-links li{font-size:6.5px;color:var(--white);position:relative;padding-left:9px;height:9.8px;font-weight:700}
.bottom-bar{left:0;top:877px;width:1200px;height:23px;background:var(--white);font-size:6.5px}
.bottom-bar .social{position:absolute;left:264px;top:7px;gap:13px}
.bottom-bar .social i{width:8px;height:8px}
.credit{left:470px;top:8px;color:#777}
.to-top{left:1002px;top:8px;color:var(--green)}
</style>
</head>
<body>

<div class="admin-bar abs">
  <span class="admin-dot abs"></span>
  <span style="left:24px">Clinician Supply Circle</span>
  <span style="left:170px">▪ 0</span>
  <span style="left:232px">+ New</span>
  <span style="left:285px">✎ Edit Page</span>
  <span class="admin-help abs">Help</span>
  <span style="left:1100px">Howdy, lena</span>
  <span class="admin-avatar abs"></span>
</div>

<header class="site-header abs">
  <div class="brand abs"><span class="brand-dot"></span>Clinician Supply Circle</div>
  <div class="nav-panel abs">
    <div class="social"><i></i><i></i><i></i></div>
    <div class="tagline abs">Financial Planning Solutions For Physicians &amp; Dentists</div>
    <ul class="main-nav abs">
      <li class="current">Home</li>
      <li>About Us</li>
      <li>Our Services ▾</li>
      <li>Resource Center</li>
      <li>Blog</li>
    </ul>
  </div>
</header>

<section class="hero abs" role="img" aria-label="Photo of hands reviewing a printed financial document on a desk">
  <div class="hero-caption abs"></div>
  <h1 class="abs">Extensive Resources</h1>
  <p class="abs">Our resource center provides you with the necessary information to secure your financial plans</p>
  <a class="btn abs">Read More&gt;&gt;</a>
  <svg class="arrow abs" style="left:17px" viewBox="0 0 16 26"><path d="M14 2 3 13l11 11" fill="none" stroke="#bbb" stroke-width="3"/></svg>
  <svg class="arrow abs" style="left:853px" viewBox="0 0 16 26"><path d="M2 2l11 11L2 24" fill="none" stroke="#ddd" stroke-width="3"/></svg>
  <span class="edit-tag abs">Edit</span>
</section>

<article class="feature abs" style="left:165px">
  <div class="thumb thumb-service" role="img" aria-label="Grey 3D lettering graphic reading service"></div>
  <h2>Our Services<span class="edit-tag">Edit</span></h2>
  <p>Comprehensive Personalized Service At Clinician Supply Circle, we specialize in successfully leading our clients through life's major financial events, mitigating risk and optimizing return ...</p>
  <a class="btn">Read more »</a>
</article>
<article class="feature abs" style="left:469px">
  <div class="thumb thumb-planning" role="img" aria-label="Blue graphic with the word planning"></div>
  <h2>Resource Center<span class="edit-tag">Edit</span></h2>
  <p>Our Resource Center contains a variety of media for your reading, listening and viewing pleasure. We hope you will find the material useful and informative. The Articles section contains articles and ...</p>
  <a class="btn">Read more »</a>
</article>
<article class="feature abs" style="left:773px">
  <div class="thumb thumb-blog" role="img" aria-label="Blue blog lettering graphic with a globe and pointing hand"></div>
  <h2>Blog<span class="edit-tag">Edit</span></h2>
  <p>Keeping you updated with our regular posts.</p>
  <a class="btn">Read more »</a>
</article>

<div class="rule abs"></div>

<aside class="sidebar abs">
  <h3><svg width="18" height="11" viewBox="0 0 18 11"><path d="M0 1h18M0 5.5h18M0 10h18" stroke="#2fbf4f" stroke-width="2"/></svg>Navigation</h3>
  <ul>
    <li>Disability Insurance</li><li>Life Insurance</li><li>Malpractice Insurance</li>
    <li>Business Formation Attorneys</li><li>Employment Contracts</li><li>Accountants</li>
    <li>Personal Loans</li><li>Student Loan Advisors</li><li>Retiremen Planning</li>
    <li>Physician Mortgages</li><li>Physician Recruiters</li><li>Real Estate Agents</li>
  </ul>
</aside>

<div class="intro abs">
  <p>Welcome to your most comprehensive financial planner.</p>
  <p>We know and understand the challenges and demands of growing a successful medical career, there is hardly enough time to do private research on financial planning. That is why we have aggregated all the resources and services you will need to secure your financial freedom.</p>
</div>

<footer class="site-footer abs">
  <div class="recent abs">
    <h4>✦ Recent Posts</h4>
    <ul style="margin-top:4px">
      <li>Healthinsurance</li>
      <li>Welcome to Clinician Supply Circle</li>
    </ul>
  </div>
  <div class="disclosure abs">
    <h4>Disclosure</h4>
    <p>The information resulting from the use of tools, charts, graphs, or other information on this website should not be construed, in any manner, as the receipt of, or a substitute for, personalized individual advice from CSC</p>
  </div>
  <ul class="footer-links abs">
    <li>Disability Insurance</li><li>Life Insurance</li><li>Malpractice Insurance</li>
    <li>Business Formation Attorneys</li><li>Employment Contracts</li><li>Accountants</li>
    <li>Personal Loans</li><li>Student Loan Advisors</li><li>Retiremen Planning</li>
    <li>Physician Mortgages</li><li>Physician Recruiters</li><li>Real Estate Agents</li>
  </ul>
</footer>

<div class="bottom-bar abs">
  <div class="social"><i></i><i></i><i></i></div>
  <span class="credit abs">· © 2014 Clinician Supply Circle · Designed by Plainleaf Studio ·</span>
  <span class="to-top abs">Back to top</span>
</div>

</body>
</html>
```